transgender support group needs innovative business card and logo

we are a transgender support group looking for a new logo and business card. I would like to include a Mona Lisa head (our logo), over top of, or somehow incorporate a rainbow (an LGBT symbol) arcing over the lower left third of the card, allowing for the text on the remaining part. Other designs are welcome, as this is just some guidance to start. I would like "MERIDAN" to possibly be larger the the "education association", and under that, I would like "a transgender resource" We also need room for the address, website and phone number. A bit larger, would need to be a spot for a name and title.
Meridian Learning Association, 412 Pine Hollow mill rd. Alderton pa18532 suite 346. phone 610 555 0147 contact person Marlene Osterby, president

```html
<!DOCTYPE html>
<html lang="en">
<head>
<meta charset="utf-8">
<title>Meridian Learning Association – Business Card</title>
<link href="https://fonts.googleapis.com/css2?family=Oranienbaum&family=Open+Sans:wght@400&display=swap" rel="stylesheet">
<style>
  :root {
    --stage: #000000;
    --card-white: #ffffff;
    --brand-blue: #2469ea;
    --ink: #111111;
    --mark: #1a1a1a;
  }
  * { margin: 0; padding: 0; box-sizing: border-box; }
  html, body {
    width: 1200px;
    height: 900px;
    overflow: hidden;
    background: var(--stage);
  }
  .canvas {
    position: relative;
    width: 1200px;
    height: 900px;
    background: var(--stage);
  }
  .card {
    position: absolute;
    top: 275px;
    width: 477px;
    height: 293px;
  }
  .card--front {
    left: 116px;
    background: var(--card-white);
    border-radius: 0 50px 0 50px;
  }
  .card--back {
    left: 622px;
    top: 276px;
    height: 292px;
    background: var(--brand-blue);
    border-radius: 50px 0 50px 0;
  }
  .wordmark {
    position: absolute;
    font-family: "Oranienbaum", serif;
    font-weight: 400;
    line-height: 1;
    white-space: nowrap;
  }
  .wordmark__name, .wordmark__sub { display: block; }

  .front-logo {
    position: absolute;
    left: 34px;
    top: 43px;
    display: flex;
    align-items: flex-start;
  }
  .front-logo__square {
    width: 48px;
    height: 53px;
    background: var(--mark);
    border-radius: 5px;
    margin-right: 8px;
  }
  .front-logo .wordmark {
    position: static;
    color: var(--ink);
  }
  .front-logo .wordmark__name { font-size: 33px; margin-top: -2px; }
  .front-logo .wordmark__sub { font-size: 25px; margin-top: 2px; }

  .contact {
    position: absolute;
    right: 31px;
    top: 139px;
    text-align: right;
    font-family: "Open Sans", sans-serif;
    color: var(--ink);
  }
  .contact__name {
    font-size: 18px;
    line-height: 22px;
    color: var(--brand-blue);
  }
  .contact__title {
    font-size: 12.5px;
    line-height: 16px;
  }
  .contact__address {
    margin-top: 20px;
    font-size: 12.5px;
    line-height: 17px;
    font-style: normal;
  }
  .contact__phone {
    margin-top: 16px;
    font-size: 12.5px;
    line-height: 16px;
    display: flex;
    align-items: center;
    justify-content: flex-end;
    gap: 9px;
  }
  .contact__phone-icon { width: 14px; height: 14px; display: block; }

  .back-wordmark {
    left: 90px;
    top: 106px;
    color: var(--card-white);
  }
  .back-wordmark .wordmark__name { font-size: 46px; }
  .back-wordmark .wordmark__sub { font-size: 36px; margin-top: 4px; }
</style>
</head>
<body>
<main class="canvas">
  <section class="card card--front" aria-label="Card front">
    <div class="front-logo">
      <span class="front-logo__square" aria-hidden="true"></span>
      <div class="wordmark">
        <span class="wordmark__name">MERIDIAN</span>
        <span class="wordmark__sub">Learning Association</span>
      </div>
    </div>
    <div class="contact">
      <p class="contact__name">Marlene Osterby</p>
      <p class="contact__title">President</p>
      <address class="contact__address">412 Pine Hollow mill rd.<br>Alderton qx18532 suite 346</address>
      <p class="contact__phone">
        <span>482 555 0147</span>
        <svg class="contact__phone-icon" viewBox="0 0 14 14" aria-hidden="true">
          <rect width="14" height="14" rx="2.5" fill="#2469ea"/>
          <path d="M4.2 2.8c.3-.2.7-.1.9.2l.9 1.5c.2.3.1.6-.1.8l-.6.5c.4 1 1.2 1.8 2.2 2.3l.5-.6c.2-.2.6-.3.8-.1l1.5.9c.3.2.4.6.2.9l-.5.8c-.3.4-.8.6-1.3.5C6.3 10 4 7.7 3.5 5.3c-.1-.5.1-1 .5-1.3z" fill="#ffffff"/>
        </svg>
      </p>
    </div>
  </section>

  <section class="card card--back" aria-label="Card back">
    <div class="wordmark back-wordmark">
      <span class="wordmark__name">MERIDIAN</span>
      <span class="wordmark__sub">Learning Association</span>
    </div>
  </section>
</main>
</body>
</html>
```